Post card for annual skin cancer screening exam

We are looking to design a modern, classy, clean, but fun postcard that we will send out to patients to remind them to schedule their follow up exams for our dermatology office.

It should include our logo
http://tovimek.com/design/logo/jpg/tovimek2.jpg
http://tovimek.com/design/logo/jpg/tovimek.jpg

Address
Phone number
website

We are open to your ideas on wording, as something clever is always appreciated - though this is going to both young and elderly patients - so the message must be easy to read and clear.
Updates

Font styles to use
Serif

Colors
85cae6
3176b5

Requirements
Must have
• Logo
• Office address
• Phone number
• website
• call to action message - to schedule a follow up visit

```html
<!DOCTYPE html>
<html lang="en">
<head>
<meta charset="utf-8">
<title>Tovimek Dermatology – Screening Reminder Postcard</title>
<link href="https://fonts.googleapis.com/css2?family=Open+Sans:ital,wght@0,400;0,600;0,700;1,400;1,600&display=swap" rel="stylesheet">
<style>
  :root{
    --sky:#85cae6;
    --ocean:#3176b5;
    --deep:#2a6fa8;
    --swoosh:#2f9fcb;
    --mist:#e4f2f9;
    --pale:#d6ebf5;
    --cream:#f8f8ec;
    --teal-wash:#dcefef;
    --ink:#555b60;
    --line:#c9ccd0;
    --page:#eef0f2;
  }
  *{box-sizing:border-box;margin:0;padding:0}
  html,body{width:877px;height:1200px;overflow:hidden}
  body{background:var(--page);font-family:"Open Sans",Arial,sans-serif;position:relative}
  .card{position:absolute;background:#fff;overflow:hidden;box-shadow:0 3px 10px rgba(0,0,0,.18)}
  .card svg.shapes{position:absolute;inset:0}
  .abs{position:absolute}

  /* front */
  .front{left:57px;top:45px;width:682px;height:527px}
  .front-title{left:0;right:0;top:22px;text-align:center;font-weight:700;font-size:24px;color:var(--deep);letter-spacing:.2px}
  .brand{display:flex;align-items:center;gap:10px;color:var(--ocean);font-weight:600}
  .brand-dot{flex:none;width:12px;height:12px;border-radius:50%;background:var(--sky)}
  .front-brand{left:462px;top:232px;font-size:26px;line-height:1.2}
  .front-brand .brand-name{display:block;width:160px;text-align:center}
  .consult{left:539px;top:306px;width:112px;height:112px;border-radius:50%;background:var(--mist);border:5px solid #fff;box-shadow:0 2px 8px rgba(0,0,0,.25);display:flex;align-items:center;justify-content:center;text-align:center;color:var(--deep);font-size:15px;line-height:1.25}
  .front-web{right:24px;top:446px;font-weight:700;font-size:23px;color:var(--deep)}
  .front-phone{right:24px;top:478px;font-weight:700;font-size:20px;color:var(--ink);display:flex;align-items:center;gap:6px}
  .front-cta{left:16px;top:478px;font-style:italic;font-weight:600;font-size:20px;color:var(--ink)}

  /* back */
  .back{left:137px;top:626px;width:680px;height:526px}
  .back-head{left:27px;top:98px;font-weight:600;font-size:19px;line-height:1.3;color:var(--deep)}
  .back-brand{left:88px;top:214px;font-size:19px}
  .back-copy{left:14px;width:318px;top:316px;text-align:center;font-size:14px;line-height:1.45;color:var(--ink)}
  .back-copy p+p{margin-top:12px;font-style:italic}
  .back-web{left:0;width:346px;top:456px;text-align:center;font-weight:700;font-size:23px;color:var(--deep)}
  .back-phone{left:0;width:346px;top:490px;justify-content:center;font-weight:700;font-size:18px;color:var(--ink);display:flex;align-items:center;gap:6px}
  .mail-address{left:384px;top:22px;font-size:11px;line-height:1.6;color:#222;font-style:normal}
  .stamp{left:564px;top:28px;width:96px;height:76px;border:1px solid #b9bcc0}
  .address-line{left:432px;width:228px;height:1px;background:var(--line)}
</style>
</head>
<body>

<section class="card front" aria-label="Postcard front">
  <svg class="shapes" viewBox="0 0 682 527" width="682" height="527" aria-hidden="true">
    <defs>
      <linearGradient id="portraitFade" x1="0" x2="1">
        <stop offset="0" stop-color="#7fbcd6"/>
        <stop offset=".18" stop-color="#a9d3e3"/>
        <stop offset=".35" stop-color="#5b5560"/>
        <stop offset=".5" stop-color="#e8cfc4"/>
        <stop offset=".7" stop-color="#cfe6ee"/>
        <stop offset="1" stop-color="#f8f8ec"/>
      </linearGradient>
      <linearGradient id="softEdge" x1="0" x2="1">
        <stop offset="0" stop-color="#f8f8ec" stop-opacity="0"/>
        <stop offset="1" stop-color="#f8f8ec"/>
      </linearGradient>
    </defs>
    <rect width="682" height="527" fill="var(--pale)"/>
    <rect width="682" height="100" fill="var(--mist)"/>
    <path d="M0,100 Q340,70 682,105 V330 Q360,470 0,395 Z" fill="var(--cream)"/>
    <path d="M0,100 Q200,82 450,90 V432 Q200,440 0,395 Z" fill="url(#portraitFade)"/>
    <rect x="380" y="88" width="70" height="345" fill="url(#softEdge)"/>
    <path d="M0,100 Q340,70 682,105" fill="none" stroke="var(--swoosh)" stroke-width="4"/>
    <path d="M0,395 Q360,470 682,330 V345 Q360,490 0,412 Z" fill="var(--swoosh)"/>
    <path d="M0,412 Q360,490 682,345 V356 Q360,500 0,424 Z" fill="var(--sky)" opacity=".7"/>
  </svg>
  <div class="abs" role="img" aria-label="Photo of a woman in profile with splashing water" style="left:0;top:90px;width:450px;height:320px"></div>
  <h1 class="abs front-title">REMINDER: ANNUAL SKIN CANCER SCREENING EXAM</h1>
  <div class="abs brand front-brand"><span class="brand-dot"></span><span class="brand-name">Tovimek<br>Dermatology</span></div>
  <div class="abs consult">CONSULT<br>US ONLINE</div>
  <div class="abs front-cta">Schedule Your Exam</div>
  <div class="abs front-web">www.tovimek.com</div>
  <div class="abs front-phone">
    <svg width="20" height="20" viewBox="0 0 20 20" aria-hidden="true"><circle cx="10" cy="10" r="9" fill="none" stroke="currentColor" stroke-width="1.6"/><path d="M6.5 5.5l2 0 .8 2.3-1.2.9a6 6 0 0 0 2.7 2.7l.9-1.2 2.3.8 0 2a1 1 0 0 1-1.1 1A8 8 0 0 1 5.5 6.6a1 1 0 0 1 1-1.1z" fill="currentColor"/></svg>
    (516) 555-0148 (CARE)
  </div>
</section>

<section class="card back" aria-label="Postcard back">
  <svg class="shapes" viewBox="0 0 680 526" width="680" height="526" aria-hidden="true">
    <defs>
      <linearGradient id="waterFade" x1="0" y1="0" x2="0" y2="1">
        <stop offset="0" stop-color="#ffffff"/>
        <stop offset=".55" stop-color="#e3f0f7"/>
        <stop offset="1" stop-color="#b6d9ea"/>
      </linearGradient>
      <linearGradient id="bubbleTone" x1="0" x2="1">
        <stop offset="0" stop-color="#e3f0f7" stop-opacity="0"/>
        <stop offset=".5" stop-color="#8ec3da"/>
        <stop offset="1" stop-color="#e3f0f7" stop-opacity="0"/>
      </linearGradient>
      <clipPath id="leftPanel"><path d="M0,0 H320 Q440,263 320,526 H0 Z"/></clipPath>
    </defs>
    <g clip-path="url(#leftPanel)">
      <rect width="680" height="186" fill="url(#waterFade)"/>
      <rect x="170" y="60" width="150" height="126" fill="url(#bubbleTone)" opacity=".7"/>
      <rect y="186" width="680" height="92" fill="#fff"/>
      <rect y="278" width="680" height="150" fill="var(--teal-wash)"/>
      <rect y="428" width="680" height="98" fill="var(--pale)"/>
    </g>
    <path d="M320,0 Q440,263 320,526" fill="none" stroke="var(--sky)" stroke-width="14"/>
    <path d="M335,0 Q462,263 335,526" fill="none" stroke="var(--swoosh)" stroke-width="8"/>
  </svg>
  <div class="abs" role="img" aria-label="Photo of bubbles rising under water" style="left:170px;top:60px;width:150px;height:126px"></div>
  <h2 class="abs back-head">BE GOOD<br>TO YOUR SKIN</h2>
  <div class="abs brand back-brand"><span class="brand-dot"></span>Tovimek Dermatology</div>
  <div class="abs back-copy">
    <p>We offer a wide variety of information to help you learn about your skin condition from a source you can trust.</p>
    <p>Schedule a consultation, and take the first step toward looking and feeling your best.</p>
  </div>
  <div class="abs back-web">www.tovimek.com</div>
  <div class="abs back-phone">
    <svg width="18" height="18" viewBox="0 0 20 20" aria-hidden="true"><circle cx="10" cy="10" r="9" fill="none" stroke="currentColor" stroke-width="1.6"/><path d="M6.5 5.5l2 0 .8 2.3-1.2.9a6 6 0 0 0 2.7 2.7l.9-1.2 2.3.8 0 2a1 1 0 0 1-1.1 1A8 8 0 0 1 5.5 6.6a1 1 0 0 1 1-1.1z" fill="currentColor"/></svg>
    (516) 555-0148 (CARE)
  </div>
  <address class="abs mail-address">Tovimek Dermatology<br>72 Harbor Crest Road;<br>Glenmore NY 11950</address>
  <div class="abs stamp" aria-label="Stamp area"></div>
  <div class="abs address-line" style="top:234px"></div>
  <div class="abs address-line" style="top:277px"></div>
  <div class="abs address-line" style="top:320px"></div>
  <div class="abs address-line" style="top:362px"></div>
</section>

</body>
</html>
```